QRVoltana Wendlio Mobile Experience

Design the following Observation and Care Path mobile app pages so they are very modern, cool and engaging.
We would also like to modernize our current splash experience (attached).

Observation and Care Path wireframes:
https://k4mzq2.plorvex.com/#g=1&p=observations__-_categories

DO NOT SUBMIT LOGO REDESIGNS. Submit all screens for the above wireframes. If you can improve the Splash screen this is a bonus. Use the same color scheme and logo.

Competitive sample:
https://apps.trivelstore.com/store/apps/details?id=com.zorquin.iphone

```html
<!DOCTYPE html>
<html lang="en">
<head>
<meta charset="utf-8">
<title>Submit Observation</title>
<link rel="stylesheet" href="https://fonts.googleapis.com/css2?family=Lato:wght@400;700;900&family=Fira+Sans:wght@400&display=swap">
<style>
  :root {
    --orange: #fba21f;
    --orange-mid: #f2a230;
    --blue: #6bb3d1;
    --white: #ffffff;
    --tab-muted: #c0c0c0;
    --text: #3a3a3a;
    --alert-bg: #fdeceb;
    --divider: #ececec;
    --chevron: #6bb3d1;
  }
  * { margin: 0; padding: 0; box-sizing: border-box; }
  html, body { width: 675px; height: 1200px; overflow: hidden; }
  body {
    position: relative;
    background: linear-gradient(180deg, var(--orange) 0%, var(--orange-mid) 14%, #d8a85a 30%, #a8ad8e 45%, var(--blue) 60%, var(--blue) 100%);
    font-family: "Fira Sans", sans-serif;
    color: var(--text);
  }
  .app-bar { position: absolute; top: 0; left: 0; width: 675px; height: 120px; }
  .app-bar__back { position: absolute; left: 38px; top: 44px; }
  .app-bar__title {
    position: absolute; left: 0; right: 0; top: 42px; text-align: center;
    font-family: "Lato", sans-serif; font-weight: 700; font-size: 26px; color: var(--white);
  }
  .app-bar__action { position: absolute; top: 39px; }
  .app-bar__action--help { left: 550px; }
  .app-bar__action--add { left: 614px; }

  .sheet {
    position: absolute; left: 20px; top: 126px; width: 635px; height: 1053px;
    background: var(--white); border-radius: 14px; overflow: hidden;
  }
  .tabs { position: absolute; top: 0; left: 0; right: 0; height: 110px; }
  .tab {
    position: absolute; top: 44px; white-space: nowrap;
    font-family: "Lato", sans-serif; font-weight: 900; font-size: 24px; letter-spacing: 1px;
    color: var(--tab-muted);
  }
  .tab--active { color: var(--orange); }
  .tab__indicator {
    position: absolute; left: 417px; top: 87px; width: 86px; height: 5px;
    background: var(--orange); border-radius: 3px;
  }
  .alert {
    position: absolute; left: 0; right: 0; top: 110px; height: 111px;
    background: var(--alert-bg); padding-left: 30px;
    display: flex; align-items: center; font-size: 25px; letter-spacing: 0.3px;
  }
  .question {
    position: absolute; left: 26px; width: 584px;
    font-size: 22px; line-height: 30px; letter-spacing: 0.2px;
  }
  .question--divided { border-bottom: 2px solid var(--divider); }
  .question__chevron { position: absolute; left: 588px; }
</style>
</head>
<body>
  <header class="app-bar">
    <svg class="app-bar__back" width="24" height="32" viewBox="0 0 24 32"><polyline points="18,3 5,16 18,29" fill="none" stroke="#fff" stroke-width="3" stroke-linecap="round" stroke-linejoin="round"/></svg>
    <h1 class="app-bar__title">Submit Observation</h1>
    <svg class="app-bar__action app-bar__action--help" width="42" height="42" viewBox="0 0 42 42">
      <circle cx="21" cy="21" r="19" fill="none" stroke="#fff" stroke-width="2.5"/>
      <text x="21" y="29" text-anchor="middle" font-family="Lato, sans-serif" font-size="22" font-weight="700" fill="#fff">?</text>
    </svg>
    <svg class="app-bar__action app-bar__action--add" width="42" height="42" viewBox="0 0 42 42">
      <circle cx="21" cy="21" r="19" fill="none" stroke="#fff" stroke-width="2.5"/>
      <path d="M21 11v20M11 21h20" stroke="#fff" stroke-width="2.5" stroke-linecap="round"/>
    </svg>
  </header>

  <main class="sheet">
    <nav class="tabs">
      <span class="tab" style="left:27px">CARE PLAN</span>
      <span class="tab" style="left:198px">CARE PATH</span>
      <span class="tab tab--active" style="left:366px">OBSERVATIONS</span>
      <span class="tab" style="left:586px; opacity:0.6">NOTES</span>
      <span class="tab__indicator"></span>
    </nav>

    <div class="alert">No refills available from the pharmacy</div>

    <div class="question question--divided" style="top:248px; height:60px">Does the Patient have enough medication for the week?
      <svg class="question__chevron" style="top:8px" width="14" height="20" viewBox="0 0 14 20"><polyline points="3,3 10,10 3,17" fill="none" stroke="var(--chevron)" stroke-width="3"/></svg>
    </div>
    <div class="question question--divided" style="top:334px; height:64px">Does the Patient have enough medication for today and tomorrow?
      <svg class="question__chevron" style="top:8px" width="14" height="20" viewBox="0 0 14 20"><polyline points="3,3 10,10 3,17" fill="none" stroke="var(--chevron)" stroke-width="3"/></svg>
    </div>
    <div class="question" style="top:423px; height:32px">Does Patient have enough medication for today?
      <svg class="question__chevron" style="top:6px" width="14" height="20" viewBox="0 0 14 20"><polyline points="3,3 10,10 3,17" fill="none" stroke="var(--chevron)" stroke-width="3"/></svg>
    </div>
  </main>
</body>
</html>
```